Web design for our new company

We need a web design for our product and for our company.
And the main is our Product tool called "veltor".
----------------------------------------------------------
[Our company's Goal]
Make organization’s communication smooth and healthy with transparency and efficiency for works and tasks in all levels with our workflow tool.

[Our Mission]
Our mission is to achieve business goals with customers.
We work together to identify the goals for your company, guides your strategy and bring the technology answers which best fit to achieve the goals.

[What we do]
We have a workflow tool "veltor"
- Very simple end-user configurable workflow for any company processes
(Targeting small-med size company)
- Graphical & fun features for startup users
- Simple and easy task control with outlook e-mail look & feel
- Non charged skill up guidance
- Additional features with;
Multiple delegation
Clear status for each owner
Task owner management console with due date reminders&reporting

Others
1. System Development & Implementation Service
Our client list includes a wide variety of small to medium to major sized enterprises.
We can offer from full-scratch based development to packaged system implementation.

2. Project Management(PM) Service
We will provide end-to-end PM service with experienced PM.
Our service is not only “managing” but “leading” to bring success to achieve the goal.

3.Consultation Service

Consulting services to a wide range of fields such as creating business strategy, business process Kaizen, IT system consultation and change management.

Target Market(s)

Business to Business
Mainly to medium size - startup company

Industry/Entity Type

It Company

Coding

Coded - Design and coding required

Number of Pages Required

5+ page

Colors
0255a3
33a6d7
86cfc6
33b8a4
add136
cadf82
fbf289
fee18a
faa54b

Requirements
Must have
• We need Pages for
• Company mission
• Service Overview
• Contact
• Privacy Policy
• Terms and Conditions
• =========================
• As there were some questions, I add followings.---------
• 1. File Format
• We are going to use Amazon web services to upload finished web files.
• The finished files should be ready to use by simply replacing images and text.
• Please provide me "easy to handle" template with "sophisticated design".
• Thanks!
• 2. Multiple Languages
• We need buttons for changing language.
• We will have this translated to German, English and Japanese.
• Thank you so much!!
Nice to have
• These are current Logos and will be a next project to revise them...
• Attached Company Profile and Logo design
• 1. Company Profile
• 2. Our Company Logo
• 3. Our Product Logo -> This is most close to our image of design base.
• 4. Product Logo for PPT Header
• All just for your reference.
• ---------
• As there were some request, I added attachment as for contents for Our mission page.
Should not have
• I hope to see some unique designs.
• (Sorry please ignore my last update as I checked with our CEO.
• Bootstrap is absolutely good template.)

```html
<!DOCTYPE html>
<html lang="en">
<head>
<meta charset="utf-8">
<title>Corvane – Business Consulting &amp; veltor Workflow</title>
<link href="https://fonts.googleapis.com/css2?family=Arimo:wght@400;700&display=swap" rel="stylesheet">
<style>
  :root{
    --bg:#ffffff;
    --hero:#1b1b1b;
    --hero-top:#141414;
    --map:#222222;
    --hero-text:#b9b9b9;
    --accent:#add136;
    --blue:#0a6fba;
    --olive:#7d8e1b;
    --ink:#1a1a1a;
    --footer:#2f313a;
    --footer-base:#26282f;
    --footer-text:#ffffff;
    --social:#35527f;
  }
  html,body{margin:0;padding:0;width:1200px;height:1200px;overflow:hidden;background:var(--bg);}
  body{font-family:"Arimo",Arial,sans-serif;color:var(--ink);}
  .stage{position:absolute;left:0;top:0;width:1500px;height:1500px;transform:scale(.8);transform-origin:0 0;}
  .abs{position:absolute;}
  .page{position:absolute;left:340px;top:0;width:818px;height:1500px;}

  /* hero */
  .hero{position:absolute;left:340px;top:0;width:818px;height:435px;background:var(--hero);}
  .hero__nav-band{position:absolute;left:0;top:0;width:100%;height:63px;background:var(--hero-top);}
  .hero__map{position:absolute;left:200px;top:140px;width:385px;height:230px;border-radius:45% 40% 50% 35%;background:radial-gradient(ellipse at center,var(--map) 0%,rgba(34,34,34,.6) 60%,rgba(27,27,27,0) 100%);}
  .brand{position:absolute;left:90px;top:92px;display:flex;align-items:center;gap:10px;}
  .brand__dot{width:18px;height:18px;border-radius:50%;background:var(--accent);}
  .brand__name{font-size:26px;font-weight:700;color:var(--accent);}
  .nav{position:absolute;right:88px;top:25px;display:flex;gap:17px;font-size:12.5px;color:#fff;}
  .nav a{color:#fff;text-decoration:none;}
  .nav a.is-active{color:var(--accent);}
  .hero__title{position:absolute;left:89px;top:243px;margin:0;font-size:24.5px;line-height:29px;font-weight:700;color:var(--hero-text);}
  .btn{position:absolute;background:var(--blue);color:#fff;font-size:12.5px;height:33px;line-height:33px;padding:0 11px;box-sizing:border-box;text-decoration:none;}

  .section-title{position:absolute;margin:0;font-size:20px;font-weight:400;transform:translateX(-50%);white-space:nowrap;}
  .service-ring{position:absolute;width:210px;height:210px;}
  .service-label{position:absolute;font-size:9px;white-space:nowrap;transform:translateX(-50%);}
  .service-text{position:absolute;top:729px;width:200px;font-size:12.3px;line-height:14.7px;margin:0;}

  .profile-photo{position:absolute;left:428px;top:922px;width:138px;height:138px;}
  .profile-text{position:absolute;left:583px;top:923px;width:335px;font-size:12.3px;line-height:14.7px;margin:0;}
  .mission-text{position:absolute;left:500px;top:1122px;width:475px;text-align:center;font-size:12.3px;line-height:14.8px;margin:0;}

  /* footer */
  .footer{position:absolute;left:340px;top:1235px;width:818px;height:265px;background:var(--footer);color:var(--footer-text);}
  .footer__base{position:absolute;left:0;top:230px;width:100%;height:35px;background:var(--footer-base);}
  .footer h4{position:absolute;margin:0;font-size:12.5px;font-weight:400;}
  .footer p{position:absolute;margin:0;font-size:9px;line-height:11.5px;}
  .footer__product-name{color:var(--blue);font-weight:700;font-size:12px;}
  .footer__map{position:absolute;left:302px;top:45px;width:104px;height:54px;background:linear-gradient(135deg,#cfe0c4,#eceae3 55%,#e7dccf);}
  .footer__links{position:absolute;left:465px;top:51px;margin:0;padding:0;list-style:none;font-size:9px;}
  .footer__links li{height:19.2px;}
  .footer__links a{color:#fff;text-decoration:underline;}
  .footer__email{position:absolute;left:627px;top:50px;width:99px;height:24px;background:#fff;color:#333;font-size:9px;line-height:24px;padding-left:9px;box-sizing:border-box;}
  .footer__submit{position:absolute;left:629px;top:95px;width:47px;height:23px;background:var(--blue);font-size:9px;line-height:23px;text-align:center;}
  .footer__copy{position:absolute;left:90px;top:244px;font-size:9px;}
  .social{position:absolute;top:234px;width:22px;height:22px;border-radius:50%;background:var(--social);}
</style>
</head>
<body>
<div class="stage">

  <header class="hero">
    <div class="hero__nav-band"></div>
    <div class="hero__map" role="img" aria-label="Faint world map silhouette in the background"></div>
    <div class="brand"><span class="brand__dot"></span><span class="brand__name">Corvane</span></div>
    <nav class="nav">
      <a class="is-active" href="#">Home</a>
      <a href="#">What We Do</a>
      <a href="#">Company Profile</a>
      <a href="#">Products</a>
      <a href="#">Contact Us</a>
    </nav>
    <h1 class="hero__title">We Are Here to Assist<br>You In Achieving Your<br>Business Goals</h1>
    <a class="btn" href="#" style="left:91px;top:348px;">Learn More</a>
  </header>

  <h2 class="section-title" style="left:745px;top:462px;">What We DO</h2>

  <svg class="abs" style="left:0;top:0" width="1500" height="760" aria-hidden="true">
    <g fill="none" stroke="var(--olive)" stroke-width="1.6">
      <path d="M441 570 A100 100 0 0 1 623 570"/><path d="M441 656 A100 100 0 0 0 623 656"/>
      <path d="M658 567 A100 100 0 0 1 837 567"/><path d="M658 661 A100 100 0 0 0 837 661"/>
      <path d="M879 567 A100 100 0 0 1 1060 571"/><path d="M879 661 A100 100 0 0 0 1058 659"/>
    </g>
    <!-- PM icon -->
    <g fill="#000">
      <rect x="502" y="577" width="70" height="46" rx="3"/>
      <rect x="507" y="582" width="60" height="36" fill="#fff"/>
      <rect x="516" y="587" width="18" height="24"/>
      <rect x="544" y="590" width="14" height="12"/>
      <circle cx="505" cy="603" r="8"/>
      <path d="M488 632 Q490 613 505 613 L525 606 L528 612 L515 622 L515 632 Z"/>
    </g>
    <!-- dev icon -->
    <g>
      <rect x="709" y="575" width="68" height="48" fill="none" stroke="#000" stroke-width="5"/>
      <rect x="736" y="623" width="12" height="6"/>
      <rect x="726" y="629" width="32" height="4"/>
      <circle cx="742" cy="600" r="6" fill="none" stroke="#000" stroke-width="3"/>
      <circle cx="751" cy="590" r="4" fill="none" stroke="#000" stroke-width="2.5"/>
      <path d="M765 610 L790 634 M790 610 L765 634" stroke="#000" stroke-width="4"/>
    </g>
    <!-- consult icon -->
    <g fill="#000">
      <circle cx="966" cy="600" r="22"/>
      <circle cx="966" cy="600" r="9" fill="#fff"/>
      <path d="M926 604 Q940 622 970 628 L996 624 L1005 636 L970 638 Q938 632 926 610 Z"/>
    </g>
  </svg>
  <span class="service-label" style="left:530px;top:638px;">Project Management(PM) Service</span>
  <span class="service-label" style="left:747px;top:640px;">System Development &amp; Implementation Service</span>
  <span class="service-label" style="left:966px;top:640px;">Consultation Service</span>

  <p class="service-text" style="left:428px;">We will provide end-to-end PM service with experienced PM. Our service is not only “managing” but “leading” to bring success to achieve the goal.</p>
  <p class="service-text" style="left:648px;">Our client list includes a wide variety of small to medium to major sized enterprises.We can offer from full scratch based development to packaged system implementation.</p>
  <p class="service-text" style="left:865px;">Consulting services to a wide range of fields such as creating business strategy, business process Kaizen, IT system consultation and change management.</p>
  <a class="btn" href="#" style="left:428px;top:820px;">Learn More</a>
  <a class="btn" href="#" style="left:648px;top:820px;">Learn More</a>
  <a class="btn" href="#" style="left:867px;top:820px;">Learn More</a>

  <h2 class="section-title" style="left:765px;top:881px;">Company Profile</h2>
  <svg class="profile-photo" viewBox="0 0 138 138" role="img" aria-label="Photo of two business colleagues working at a laptop">
    <defs><linearGradient id="photoTone" x1="0" y1="0" x2="1" y2="1"><stop offset="0" stop-color="#d9e3ec"/><stop offset=".55" stop-color="#8a8f98"/><stop offset="1" stop-color="#c9ccd1"/></linearGradient></defs>
    <polygon points="40,0 112,6 138,62 112,122 52,138 4,104 0,44" fill="url(#photoTone)"/>
  </svg>
  <p class="profile-text">Lorem ipsum dolor sit amet, consectetur adipisicing elit, sed do eiusmod tempor incididunt ut labore et dolore magna aliqua. Ut enim ad minim veniam, quis nostrud exercitation ullamco laboris nisi ut aliquip ex ea commodo consequat. Duis aute irure dolor in reprehenderit in voluptate velit esse</p>
  <a class="btn" href="#" style="left:585px;top:1007px;">Learn More</a>

  <h2 class="section-title" style="left:743px;top:1080px;">Our Mission</h2>
  <p class="mission-text">Our mission is to achieve business goals with customers.<br>We work together to identify the goals for your company, guides your strategy and bring the technology answers which best fit to achieve the goals.</p>

  <footer class="footer">
    <h4 style="left:90px;top:23px;">Product Overview <span class="footer__product-name">veltor</span></h4>
    <p style="left:88px;top:44px;width:160px;">We have a workflow tool "veltor"<br>&nbsp;Very simple end-user configurable workflow for any company processes (Targeting small-med size company)</p>
    <a class="btn" href="#" style="left:88px;top:122px;">Learn More</a>

    <h4 style="left:302px;top:23px;">Coporate Office</h4>
    <div class="footer__map" role="img" aria-label="Small street map of the office location"></div>
    <svg class="abs" style="left:355px;top:59px" width="14" height="20" aria-hidden="true"><path d="M7 20 L1 10 A7 7 0 1 1 13 10 Z" fill="#1d3a5a"/><circle cx="7" cy="7" r="2.5" fill="#fff"/></svg>
    <p style="left:302px;top:115px;">A – 8120 Feldmark<br>Mühlgasse 7</p>
    <p style="left:302px;top:146px;line-height:13.5px;">C.E.O. Ing. Lukas Brenner<br>Establishment 2013<br>Industry IT Consulting and<br>System development</p>

    <h4 style="left:465px;top:25px;">Useful Links</h4>
    <ul class="footer__links">
      <li>- <a href="#">Homepage</a></li>
      <li>- <a href="#">About us</a></li>
      <li>- <a href="#">Product Overview</a></li>
      <li>- <a href="#">Pricing</a></li>
      <li>- <a href="#">Policy</a></li>
    </ul>

    <h4 style="left:627px;top:25px;">Newsletter</h4>
    <div class="footer__email">Email</div>
    <div class="footer__submit">Submit</div>

    <div class="footer__base"></div>
    <span class="footer__copy">CopyRight 2018 &nbsp;Corvane All Rights Reserved</span>
    <span class="social" style="left:651px;"></span>
    <span class="social" style="left:677px;"></span>
    <span class="social" style="left:703px;"></span>
  </footer>

</div>
</body>
</html>
```